Corporate consulting business needs a business card

I want a professional business card.... surprise me

Updates

Reason: i dont think 2 days is enough

Target Market(s)

Corprorate and Not for Profit firms and organisations

Industry/Entity Type

Consulting

Contact Information for Business Card

Logo
Corporate Consulting Services
On Time, On Budget, Beyond Expectation
Tovan Presfield
Director
0427 31 94 62 (Larger)
tovan@tp-advisory.com.au
www.tp-advisory.com.au
include little icons beside the contact info:

- Envelope = email
- Phone = phone
- Globe = website

Font styles to use
Serif
Sans Serif

Requirements
Must have
• Professional and clean
Nice to have
• you tell me

```html
<!DOCTYPE html>
<html lang="en">
<head>
<meta charset="utf-8">
<title>TP Advisory – Business Card</title>
<link rel="stylesheet" href="https://fonts.googleapis.com/css2?family=Cormorant+Garamond:wght@500&family=Josefin+Sans:wght@300;600&family=Open+Sans:wght@400;600;700&display=swap">
<style>
  :root {
    --backdrop: #ebebeb;
    --brown: #4a2814;
    --brown-text: #4e2a16;
    --white: #ffffff;
    --grey-text: #9a9a9a;
    --grey-mid: #8c8c8c;
    --divider: #b5b5b5;
    --silver-light: #f2f2f2;
    --silver-mid: #c9c9c9;
    --silver-dark: #9e9e9e;
  }
  * { box-sizing: border-box; margin: 0; padding: 0; }
  html, body {
    width: 1138px; height: 1200px; overflow: hidden;
    background: var(--backdrop);
  }
  .sheet { position: relative; width: 1138px; height: 1200px; }
  .card {
    position: absolute; left: 139px; width: 860px; height: 524px;
    box-shadow: 0 6px 18px rgba(0,0,0,0.18);
  }
  /* Front */
  .card--front {
    top: 50px; background: var(--brown);
    display: flex; flex-direction: column; align-items: center; justify-content: center;
  }
  .brand {
    display: flex; align-items: center; gap: 18px;
    font-family: "Cormorant Garamond", Georgia, serif; font-weight: 500;
    font-size: 54px; color: var(--white); letter-spacing: 3px; line-height: 1;
  }
  .brand__dot {
    width: 40px; height: 40px; border: 3px solid var(--white); border-radius: 50%; flex: none;
  }
  .brand-line {
    margin-top: 28px;
    font-family: "Cormorant Garamond", Georgia, serif; font-weight: 500;
    font-size: 30px; color: var(--white); letter-spacing: 1px;
  }
  /* Back */
  .card--back { top: 626px; background: var(--white); }
  .identity {
    position: absolute; top: 110px; right: 520px; text-align: right;
    font-family: "Josefin Sans", Arial, sans-serif; text-transform: uppercase;
  }
  .identity__first {
    font-weight: 300; font-size: 46px; color: var(--grey-text); letter-spacing: 2px; line-height: 1;
  }
  .identity__last {
    font-weight: 600; font-size: 46px; color: var(--brown-text); letter-spacing: 2px; line-height: 1.05;
  }
  .identity__role {
    font-family: "Open Sans", Arial, sans-serif; text-transform: none;
    font-size: 16px; color: var(--grey-mid); margin-top: 2px;
  }
  .divider {
    position: absolute; left: 356px; top: 96px; width: 2px; height: 176px; background: var(--divider);
  }
  .contacts {
    position: absolute; left: 380px; top: 106px; list-style: none;
    font-family: "Open Sans", Arial, sans-serif;
  }
  .contacts li { display: flex; align-items: center; gap: 12px; height: 40px; }
  .contacts svg { width: 22px; height: 22px; flex: none; }
  .contact--phone { font-weight: 700; font-size: 28px; color: var(--grey-mid); }
  .contact--email, .contact--web { font-size: 26px; color: var(--grey-mid); }
  .tagline-band {
    position: absolute; left: 0; right: 0; top: 378px; height: 92px;
    background: linear-gradient(to bottom, var(--silver-light) 0%, var(--silver-light) 34%, var(--silver-mid) 40%, var(--silver-dark) 70%, var(--silver-mid) 100%);
  }
  .tagline {
    position: absolute; left: 0; right: 0; top: 380px; text-align: center;
    font-family: "Open Sans", Arial, sans-serif; font-weight: 700; font-size: 16px;
    color: var(--brown-text); letter-spacing: 0.5px; text-transform: uppercase; line-height: 28px;
  }
</style>
</head>
<body>
<main class="sheet">
  <section class="card card--front">
    <div class="brand"><span class="brand__dot"></span><span class="brand__name">TP ADVISORY</span></div>
    <p class="brand-line">CONSULTING SERVICES</p>
  </section>

  <section class="card card--back">
    <div class="identity">
      <p class="identity__first">Tovan</p>
      <p class="identity__last">Presfield</p>
      <p class="identity__role">Director</p>
    </div>
    <div class="divider"></div>
    <ul class="contacts">
      <li class="contact--phone">
        <svg viewBox="0 0 24 24" aria-hidden="true"><path fill="#4e2a16" d="M6.6 10.8c1.4 2.8 3.8 5.1 6.6 6.6l2.2-2.2c.3-.3.7-.4 1-.2 1.1.4 2.3.6 3.6.6.6 0 1 .4 1 1V20c0 .6-.4 1-1 1C10.6 21 3 13.4 3 4c0-.6.4-1 1-1h3.5c.6 0 1 .4 1 1 0 1.3.2 2.5.6 3.6.1.3 0 .7-.2 1z"/></svg>
        0427 31 94 62
      </li>
      <li class="contact--email">
        <svg viewBox="0 0 24 24" aria-hidden="true"><rect x="2" y="5" width="20" height="14" rx="1.5" fill="#4e2a16"/><path d="M3 6l9 7 9-7" fill="none" stroke="#fff" stroke-width="1.6"/></svg>
        tovan@tp-advisory.com.au
      </li>
      <li class="contact--web">
        <svg viewBox="0 0 24 24" aria-hidden="true"><circle cx="12" cy="12" r="10" fill="#4e2a16"/><g fill="none" stroke="#fff" stroke-width="1.3"><ellipse cx="12" cy="12" rx="4" ry="9"/><path d="M3 12h18M5 7h14M5 17h14"/></g></svg>
        www.tp-advisory.com.au
      </li>
    </ul>
    <div class="tagline-band"></div>
    <p class="tagline">On Time | On Budget | Beyond Expectation</p>
  </section>
</main>
</body>
</html>
```